label update for bottle change

The goal is to adapt the label's design and shape to the new bottle, maintaining its defining elements such as the font, vertical name, company logo, background pattern, and color. The new design should not be identical to the old one, but rather an evolution of it. The gold stripe on the bottom is not mandatory, but the writing "VALDORIA DEL MONTE / EST. 1886" must be retained, slightly enlarged.

The font name is: Brandon Text

```html
<!DOCTYPE html>
<html lang="it">
<head>
<meta charset="utf-8">
<title>Amaro di Carattere – Carciofo label</title>
<link rel="stylesheet" href="https://fonts.googleapis.com/css2?family=Josefin+Sans:wght@400;600;700&display=swap">
<style>
  :root {
    --canvas-bg: #ffffff;
    --label-dark: #262626;
    --ink-white: #ffffff;
    --gold-text: #e2b93b;
    --gold-light: #f7e36a;
    --gold-mid: #e6c43a;
    --gold-deep: #b98a1c;
    --band-ink: #1c1a14;
  }
  * { margin: 0; padding: 0; box-sizing: border-box; }
  html, body {
    width: 1200px; height: 1012px; overflow: hidden;
    background: var(--canvas-bg);
  }
  body { position: relative; font-family: "Josefin Sans", sans-serif; }

  .label {
    position: absolute; left: 276px; top: 75px;
    width: 648px; height: 862px;
    background: var(--label-dark);
    overflow: hidden;
  }
  .label__pattern {
    position: absolute; inset: 0 0 82px 0;
    background: var(--label-dark);
  }

  .maker {
    position: absolute; left: 295px; top: 66px; width: 300px;
    color: var(--ink-white);
  }
  .maker__kicker {
    font-size: 17px; font-weight: 700; letter-spacing: 7.4px;
    line-height: 1;
  }
  .maker__name {
    margin-top: 6px;
    font-size: 44px; font-weight: 700; letter-spacing: 1px;
    line-height: 1;
    white-space: nowrap;
  }

  .vertical {
    position: absolute;
    transform-origin: 0 0;
    transform: rotate(-90deg);
    white-space: nowrap;
    line-height: 1;
  }
  .product-type {
    left: 106px; top: 746px;
    color: var(--gold-text);
    font-size: 31px; font-weight: 600; letter-spacing: 6.3px;
  }
  .product-name {
    left: 152px; top: 748px;
    color: var(--ink-white);
    font-size: 112px; font-weight: 700; letter-spacing: 6px;
  }

  .artwork {
    position: absolute; left: 293px; top: 261px;
    width: 342px; height: 513px;
    background: radial-gradient(ellipse at 45% 35%, var(--gold-light), var(--gold-mid) 55%, var(--gold-deep));
    border-radius: 48% 48% 22% 22% / 40% 40% 14% 14%;
  }

  .origin-band {
    position: absolute; left: 0; bottom: 0;
    width: 648px; height: 82px;
    background: linear-gradient(90deg, var(--gold-deep) 0%, var(--gold-mid) 18%, var(--gold-light) 60%, var(--gold-mid) 82%, var(--gold-deep) 100%);
  }
  .origin-band__text {
    position: absolute; right: 47px; top: 30px;
    color: var(--band-ink);
    font-size: 17px; font-weight: 700; letter-spacing: 1.8px;
    line-height: 1;
    white-space: nowrap;
  }
</style>
</head>
<body>
  <main class="label">
    <div class="label__pattern" role="img" aria-label="Dark background with a subtle repeating scale pattern"></div>

    <div class="maker">
      <p class="maker__kicker">FABBRICA LIQUORI</p>
      <p class="maker__name">F.LLI CORVANI</p>
    </div>

    <p class="vertical product-type">AMARO DI CARATTERE</p>
    <h1 class="vertical product-name">CARCIOFO</h1>

    <div class="artwork" role="img" aria-label="Gold engraved illustration of an artichoke"></div>

    <footer class="origin-band">
      <p class="origin-band__text">VALDORIA DEL MONTE &nbsp;/&nbsp; EST. 1886</p>
    </footer>
  </main>
</body>
</html>
```